Parity Skills Forum needs a brochure to attract participants to its trainings

We need a flyer for our EU-funded project called " Parity Skills Forum" and it aims at increasing and developing skills of researchers and university staff members who are implementing measures towards gender equality in their institutions through our offered training programs. The final design should communicate gender equality for Research and Innovation centres and universities. This flyer will be distributed during conferences and events to our audience (mainly gender experts, researchers, administrative staff of universities, etc.) in order to provide the basic information about the project and options to get involved in the different trainings. We are attaching files to provide you with the concrete information on our requirements:- PS Forum flyer content.ppt: includes the content we would like to include in the flyer. There is also the URL to the project website and the different social media channels. - Project logo.zip: the project logo and guidelines as we would like to use colors that belong to the project logo color range. - Partners' logos.zip: Logos that will be included- EU flag: You can download different resolution files of the flag here: https://unionvexa.org/about-union/emblems/banner_en -Regarding the images or graphics that you may include in the brochure we wouldn’t like to propose any because we do not want to limitate your imagination.

As it was not mentioned and we received a lot of questions about it, we prefer the flyer to be double-sided and in A5

Font styles to use
Serif
Sans Serif

Colors

Designer to choose colors to be used in the design.

Requirements
Nice to have
• At least 4 pages
Should not have
• We would not like to see as dominant colours the classic blue and pink.

```html
<!DOCTYPE html>
<html lang="en">
<head>
<meta charset="utf-8">
<title>Parity Skills Forum – Inside Spread</title>
<link rel="stylesheet" href="https://fonts.googleapis.com/css2?family=Montserrat:wght@600;700;800&family=Nunito+Sans:wght@300;400;600;700&display=swap">
<style>
:root{
  --teal:#17b9cf;
  --magenta:#c9205f;
  --ink:#2b2b33;
  --paper:#fbfbfc;
  --stage:#e9ecf1;
  --rule:#cfd4da;
}
*{margin:0;padding:0;box-sizing:border-box}
html,body{width:1200px;height:1200px;overflow:hidden;background:var(--stage)}
body{font-family:"Nunito Sans",sans-serif;color:var(--ink)}
.spread{position:absolute;left:0;top:177px;width:1200px;height:846px;overflow:hidden;
  background:linear-gradient(160deg,#f7f3f1 0%,#f3f6f8 45%,#eef4f7 100%)}
.abs{position:absolute}
.band-top{position:absolute;top:0;height:24px;background:var(--teal)}
.fold{position:absolute;left:600px;top:0;height:846px;border-left:1px dashed #9aa0a8}
.h-title{font-family:"Montserrat",sans-serif;font-weight:800;color:var(--teal);font-size:29px;letter-spacing:.3px;line-height:1}
.rule{position:absolute;height:2px;background:var(--magenta)}
.rule.teal{background:var(--teal)}
.lead{font-family:"Montserrat",sans-serif;font-weight:700;color:var(--magenta);font-size:11px;line-height:15px;text-transform:uppercase}
.body{font-size:11px;line-height:15px}
.body .dot{color:var(--magenta)}
.teal-box{background:var(--teal);color:#fff}
.box-text{font-family:"Montserrat",sans-serif;font-weight:700;font-size:13.5px;line-height:18.6px;text-transform:uppercase}
.offer{position:absolute;left:24px;width:268px;display:flex;gap:10px;font-family:"Montserrat",sans-serif;font-weight:600;font-size:11px;line-height:15.3px;text-transform:uppercase}
.offer svg{flex:none;width:18px;height:18px;margin-top:-1px}
.sep{position:absolute;left:53px;width:238px;height:1px;background:var(--rule)}
.stat{position:absolute;width:125px}
.stat .row{display:flex;align-items:center;gap:3px}
.stat .num{font-family:"Montserrat",sans-serif;font-weight:600;color:var(--teal);font-size:30px;line-height:1}
.stat .lbl{font-family:"Montserrat",sans-serif;font-weight:700;font-size:9px;line-height:12px;text-transform:uppercase;margin-top:6px}
.stat .sub{font-size:7px;font-weight:700;text-transform:uppercase}
.involve{position:absolute;right:26px;width:320px;display:flex;align-items:flex-start;justify-content:flex-end;gap:14px;font-weight:300;font-size:15.5px;line-height:16px;text-align:right}
.involve span{max-width:280px}
.involve svg{flex:none;width:20px;height:20px;margin-top:4px}
.visit-1{font-family:"Montserrat",sans-serif;font-weight:600;font-size:20px;line-height:24px;text-transform:uppercase}
.visit-2{font-family:"Montserrat",sans-serif;font-weight:800;font-size:31px;line-height:34px;text-transform:uppercase}
.visit-3{font-family:"Montserrat",sans-serif;font-weight:600;font-size:21px;line-height:30px}
.anyone{font-family:"Montserrat",sans-serif;font-weight:700;font-size:17.5px;line-height:25px;text-align:right;text-transform:uppercase}
.aud-label{font-family:"Montserrat",sans-serif;font-weight:700;color:var(--magenta);font-size:11.5px;text-transform:uppercase}
.aud{position:absolute;display:flex;gap:7px;font-size:12.5px;line-height:16.5px}
.aud svg{flex:none;width:18px;height:18px;margin-top:1px}
.photo-shape{position:absolute;left:0;top:0}
</style>
</head>
<body>
<svg width="0" height="0" style="position:absolute">
  <defs>
    <symbol id="tick" viewBox="0 0 20 20">
      <circle cx="10" cy="10.5" r="8" fill="none" stroke="#c9205f" stroke-width="1.6"/>
      <path d="M5.5 10.5l3.4 3.4L18 4" fill="none" stroke="#c9205f" stroke-width="2" stroke-linecap="round" stroke-linejoin="round"/>
    </symbol>
    <linearGradient id="warmPhoto" x1="0" y1="0" x2="1" y2="1">
      <stop offset="0" stop-color="#cdbfae"/><stop offset=".5" stop-color="#e6d4c2"/><stop offset="1" stop-color="#9fb7bb"/>
    </linearGradient>
    <linearGradient id="deskPhoto" x1="0" y1="0" x2="1" y2="1">
      <stop offset="0" stop-color="#3c3836"/><stop offset=".55" stop-color="#6d655d"/><stop offset="1" stop-color="#d9d4cc"/>
    </linearGradient>
    <linearGradient id="greyPhoto" x1="0" y1="0" x2="1" y2="1">
      <stop offset="0" stop-color="#6f6f6f"/><stop offset=".5" stop-color="#c9c9c9"/><stop offset="1" stop-color="#8d8d8d"/>
    </linearGradient>
  </defs>
</svg>

<main class="spread">
  <div class="band-top" style="left:0;width:380px"></div>
  <div class="band-top" style="left:820px;width:380px"></div>

  <svg class="photo-shape" width="1200" height="846" viewBox="0 0 1200 846">
    <polygon role="img" aria-label="Photo: teacher working with two pupils at a classroom table"
      points="379,-6 820,-6 820,188 600,326 379,188" fill="url(#warmPhoto)" stroke="#c9205f" stroke-width="9" stroke-linejoin="round"/>
    <polygon role="img" aria-label="Photo: students reading open books on a wooden table"
      points="434,270 551,338 551,472 434,540 317,472 317,338" fill="url(#deskPhoto)" stroke="#c9205f" stroke-width="8" stroke-linejoin="round"/>
    <polygon role="img" aria-label="Black and white photo: smiling woman in a group workshop"
      points="763,270 880,338 880,472 763,540 646,472 646,338" fill="url(#greyPhoto)" stroke="#c9205f" stroke-width="8" stroke-linejoin="round"/>
  </svg>

  <div class="fold"></div>

  <!-- Left panel -->
  <h2 class="h-title abs" style="left:24px;top:58px">THE CHALLENGE</h2>
  <div class="rule" style="left:24px;top:88px;width:281px"></div>
  <p class="lead abs" style="left:24px;top:102px;width:350px">Currently, there are many programmes, projects and a great gained knowledge and experience, but:</p>
  <div class="body abs" style="left:24px;top:136px;width:255px">
    <p><span class="dot">•</span> Gender analysis remains rarely appropriated within research projects</p>
    <p style="margin-top:2px"><span class="dot">•</span> Large differences among research performing organisations in various countries</p>
    <p style="margin-top:2px"><span class="dot">•</span> Small proportion of researchers and practitioners are familiar with theoretical and methodological concepts of gender and feminist scholarship</p>
  </div>
  <p class="lead abs" style="left:24px;top:252px;width:350px">Need: a holistic approach to structural change for gender equality in R&amp;I</p>

  <div class="teal-box abs" style="left:24px;top:304px;width:315px;height:133px;padding:12px 0 0 17px">
    <p class="box-text">The Parity Skills Forum project offers high-quality capacity-building programme on gender equality in research, innovation and higher education</p>
  </div>

  <h2 class="h-title abs" style="left:24px;top:470px">TRAINING OFFERS</h2>
  <div class="rule" style="left:24px;top:499px;width:281px"></div>

  <div class="offer" style="top:515px"><svg><use href="#tick"/></svg><span>Trainings are offered for free to those interested to understand and consider gender equality and dimension as an integral part of research and innovation.</span></div>
  <div class="sep" style="top:594px"></div>
  <div class="offer" style="top:607px"><svg><use href="#tick"/></svg><span>Find the offer which suits you best and register on<br><span style="text-transform:none">https://psforum.eu/</span></span></div>
  <div class="sep" style="top:658px"></div>
  <div class="offer" style="top:668px"><svg><use href="#tick"/></svg><span>There are different dates and locations</span></div>
  <div class="sep" style="top:704px"></div>
  <div class="offer" style="top:714px"><svg><use href="#tick"/></svg><span>Course language: English</span></div>
  <div class="offer" style="top:744px"><svg><use href="#tick"/></svg><span>Participation is free thanks to the Union Vexa.</span></div>

  <div class="stat" style="left:329px;top:546px">
    <div class="row"><svg width="52" height="52" viewBox="0 0 52 52"><rect x="2" y="2" width="48" height="48" rx="9" fill="none" stroke="#17b9cf" stroke-width="3"/><rect x="14" y="12" width="26" height="18" fill="none" stroke="#c9205f" stroke-width="3"/><circle cx="13" cy="22" r="4" fill="#c9205f"/><rect x="10" y="27" width="7" height="15" fill="#c9205f"/></svg><span class="num">28</span></div>
    <p class="lbl">Training offers</p>
  </div>
  <div class="stat" style="left:455px;top:546px">
    <div class="row"><svg width="52" height="52" viewBox="0 0 52 52"><rect x="2" y="2" width="48" height="48" rx="9" fill="none" stroke="#17b9cf" stroke-width="3"/><rect x="18" y="9" width="22" height="14" fill="#c9205f"/><circle cx="14" cy="30" r="4" fill="#c9205f"/><circle cx="26" cy="32" r="4" fill="#c9205f"/><circle cx="38" cy="32" r="4" fill="#c9205f"/><rect x="9" y="37" width="34" height="6" rx="3" fill="#c9205f"/></svg><span class="num">12</span></div>
    <p class="lbl">Workshops</p>
  </div>
  <div class="stat" style="left:329px;top:631px">
    <div class="row"><svg width="52" height="52" viewBox="0 0 52 52"><rect x="2" y="2" width="48" height="48" rx="9" fill="none" stroke="#17b9cf" stroke-width="3"/><polygon points="8,24 26,14 44,24 44,42 8,42" fill="#c9205f"/><rect x="23" y="32" width="6" height="10" fill="#fff"/><rect x="12" y="28" width="6" height="5" fill="#fff"/><rect x="34" y="28" width="6" height="5" fill="#fff"/></svg><span class="num">3</span></div>
    <p class="lbl" style="margin-top:4px">Summer schools</p>
    <p class="sub">Madrid | Dublin | Budapest</p>
  </div>
  <div class="stat" style="left:455px;top:631px;width:140px">
    <div class="row"><svg width="52" height="52" viewBox="0 0 52 52"><rect x="2" y="2" width="48" height="48" rx="9" fill="none" stroke="#17b9cf" stroke-width="3"/><rect x="14" y="9" width="24" height="32" rx="2" fill="none" stroke="#c9205f" stroke-width="3"/><line x1="20" y1="18" x2="33" y2="18" stroke="#c9205f" stroke-width="3"/><line x1="20" y1="25" x2="33" y2="25" stroke="#c9205f" stroke-width="3"/><circle cx="15" cy="38" r="5" fill="#c9205f"/></svg><span class="num">2</span></div>
    <p class="lbl">Distributed open<br>collaborative courses</p>
  </div>
  <div class="stat" style="left:329px;top:731px">
    <div class="row"><svg width="52" height="52" viewBox="0 0 52 52"><rect x="2" y="2" width="48" height="48" rx="9" fill="none" stroke="#17b9cf" stroke-width="3"/><path d="M8 14q9-4 18 2q9-6 18-2v26q-9-4-18 2q-9-6-18-2z" fill="#c9205f"/></svg><span class="num">2</span></div>
    <p class="lbl">Train-the-trainers'<br>sessions</p>
  </div>
  <div class="stat" style="left:455px;top:731px">
    <div class="row"><svg width="52" height="52" viewBox="0 0 52 52"><rect x="2" y="2" width="48" height="48" rx="9" fill="none" stroke="#17b9cf" stroke-width="3"/><rect x="10" y="16" width="24" height="22" fill="none" stroke="#c9205f" stroke-width="3"/><rect x="26" y="8" width="16" height="11" rx="3" fill="none" stroke="#c9205f" stroke-width="3"/><circle cx="19" cy="26" r="4" fill="#c9205f"/><rect x="14" y="32" width="10" height="6" fill="#c9205f"/></svg><span class="num">12</span></div>
    <p class="lbl">Webinars</p>
  </div>

  <!-- Right panel -->
  <h2 class="h-title abs" style="right:27px;top:60px">GET INVOLVED</h2>
  <div class="rule" style="left:853px;top:94px;width:321px"></div>
  <div class="involve" style="top:106px"><span>Take part in one or more offered trainings</span><svg><use href="#tick"/></svg></div>
  <div class="involve" style="top:154px"><span>Become a gender trainer</span><svg><use href="#tick"/></svg></div>
  <div class="involve" style="top:187px"><span>Become a host institution to the topic of your preference</span><svg><use href="#tick"/></svg></div>
  <div class="involve" style="top:235px"><span>Be part of the pan European gender trainers' network</span><svg><use href="#tick"/></svg></div>

  <div class="teal-box abs" style="left:880px;top:304px;width:294px;height:133px;padding:28px 0 0 16px">
    <p class="visit-1">Visit the website and</p>
    <p class="visit-2">Find out more</p>
    <p class="visit-3">https://psforum.eu/</p>
  </div>

  <h2 class="h-title abs" style="right:27px;top:473px">WHO IS IT FOR?</h2>
  <div class="rule" style="left:853px;top:505px;width:321px"></div>
  <p class="anyone abs" style="right:26px;top:515px;width:360px">Anyone interested to gender equality, but also:</p>

  <p class="aud-label abs" style="left:626px;top:593px">HR professionals</p>
  <p class="aud-label abs" style="left:896px;top:593px">Gender trainers &amp; experts</p>
  <div class="rule teal" style="left:626px;top:610px;width:548px"></div>
  <div class="aud" style="left:626px;top:617px;width:245px"><svg><use href="#tick"/></svg><span>Integration and establishment of gender-sensitive and fair recruitment and career management processes in organisations</span></div>
  <div class="aud" style="left:896px;top:617px;width:260px"><svg><use href="#tick"/></svg><span>Train-the-trainers sessions for the development of new skills</span></div>

  <p class="aud-label abs" style="left:646px;top:704px">Researchers</p>
  <p class="aud-label abs" style="left:896px;top:704px">Research performing organisations</p>
  <div class="rule teal" style="left:626px;top:721px;width:548px"></div>
  <div class="aud" style="left:626px;top:729px;width:245px"><svg><use href="#tick"/></svg><span>Training to integrate the gender dimension in their research and deepening their understanding of gender issues in R&amp;I</span></div>
  <div class="aud" style="left:896px;top:729px;width:270px"><svg><use href="#tick"/></svg><span>Recommendations for influencing the internal policies and practices of the organisations towards gender equality</span></div>

  <svg class="abs" style="left:0;top:800px" width="1200" height="46" viewBox="0 0 1200 46">
    <polygon points="0,6 0,46 250,46" fill="#c9205f"/>
    <polygon points="1200,6 1200,46 950,46" fill="#c9205f"/>
    <polygon points="180,46 600,8 1020,46" fill="#ffffff"/>
    <polygon points="235,46 600,13 965,46" fill="#17b9cf"/>
  </svg>
</main>
</body>
</html>
```